Professional BBQ Cleaning Flyer (Before & After Focus)

We need a clean, professional double-sided A5 flyer for a BBQ cleaning business.
This flyer will be handed directly to:
Property managers
Retirement villages
Over 50s communities
Resorts / body corporate
The design must feel professional, trustworthy, and easy to read β not cluttered or cheap.
π― Goal
Use a strong before & after BBQ image to show the value of the service, and position the business as reliable for communal BBQ cleaning.
π Size & Format
A5 (148 x 210mm)
Portrait (vertical)
Double-sided
Print-ready (with bleed)
π¨ Style & Branding
Colours: Red, Black, White
Clean, modern, minimal
Strong, easy-to-read fonts (important for older audience)
Plenty of white space
No emojis, no clutter, no cheap design elements
π₯ FRONT SIDE (IMPORTANT β MAIN FOCUS)
Must include:
Headline:
Professional BBQ Cleaning
For Shared & Communal Areas
Subheadline:
Keep your BBQs clean, safe, and ready for residents & guests
Main Visual :
Side-by-side BEFORE & AFTER BBQ
This is the main focus of the flyer
Must be realistic and high quality
Labels under images:
BEFORE β Greasy β’ Dirty β’ Unsafe
AFTER β Clean β’ Hygienic β’ Ready to Use
Short Bullet Points:
Deep clean of grills, burners & internal components
Ideal for retirement villages, resorts & body corporate
Multiple BBQs cleaned in one visit
Trust Line:
Fully insured & police checked
Call to Action (bottom):
Get a Quote or Book a Service
0428 593 214
www.grillshinecrew.example.au
β¬ BACK SIDE (CREDIBILITY & DETAIL)
Headline:
Trusted by Property Managers & Facilities Teams
Whatβs Included:
Full dismantle and deep clean
Removal of grease, carbon & built-up residue
Grills, burners, trays & surfaces cleaned
Reassembled and checked
Why Choose Us:
Professional, reliable service
Works around your schedule
Ideal for high-use communal BBQ areas
One-off or ongoing maintenance
Ideal For:
Retirement villages
Apartment complexes
Resorts
Body corporate properties
Closing Line:
Keep your shared BBQ areas clean, safe, and presentable year-round
Contact:
Grill Shine Crew
0428 593 214
www.grillshinecrew.example.au
grillshinecrew@mailbox.example

```html
<!DOCTYPE html>
<html lang="en">
<head>
<meta charset="utf-8">
<title>Grill Shine Crew – Flyer</title>
<link href="https://fonts.googleapis.com/css2?family=Barlow:wght@500;600;700;800&family=Krona+One&display=swap" rel="stylesheet">
<style>
:root{
  --red:#d7263d;
  --black:#0b0b0b;
  --white:#ffffff;
  --canvas:#f2f2f2;
  --line:#d9d9d9;
  --steel-dark:#4a4440;
  --steel-light:#c9ccce;
}
*{box-sizing:border-box;margin:0;padding:0}
html,body{width:1200px;height:928px;overflow:hidden;background:var(--canvas)}
body{position:relative;font-family:"Barlow",sans-serif;color:var(--black)}
.page{position:absolute;top:115px;width:492px;height:698px;background:var(--white);overflow:hidden;box-shadow:0 8px 24px rgba(0,0,0,.12)}
.page--front{left:76px}
.page--back{left:633px}
.abs{position:absolute}
.center{left:0;right:0;text-align:center}

/* brand */
.brand{display:flex;align-items:center;gap:8px}
.brand__dot{width:22px;height:22px;border-radius:50%;background:var(--red);flex:none}
.brand__name{font-weight:800;color:var(--red);text-transform:uppercase;letter-spacing:.5px;white-space:nowrap}
.front-brand{top:52px;left:0;right:0;justify-content:center}
.front-brand .brand__dot{width:34px;height:34px}
.front-brand .brand__name{font-size:30px}

/* front headline */
.kicker{top:125px;font-size:19px;font-weight:800;color:var(--red);letter-spacing:9px;padding-left:9px}
.headline{top:148px;font-family:"Krona One",sans-serif;font-size:32px;letter-spacing:-.5px}
.subhead{top:186px;font-size:25px;font-weight:800;color:var(--red);letter-spacing:-.2px}
.tagline{top:218px;font-size:11.5px;font-weight:500}

/* before/after */
.photo{top:242px;width:198px;height:221px;border-radius:22px 22px 0 0;overflow:hidden}
.photo--before{left:36px;background:linear-gradient(170deg,#8d8782 0%,var(--steel-dark) 45%,#2a2624 100%)}
.photo--after{left:251px;background:linear-gradient(170deg,#e4e6e7 0%,var(--steel-light) 50%,#5a5f63 100%)}
.photo__tab{position:absolute;left:0;top:0;width:41px;height:109px;background:var(--red);border-radius:22px 0 22px 0;display:flex;align-items:center;justify-content:center}
.photo__tab span{transform:rotate(-90deg);color:var(--white);font-weight:800;font-size:21px;letter-spacing:.5px}
.chips{position:absolute;bottom:0;left:14px;display:flex;gap:2px}
.chip{background:var(--black);color:var(--white);font-weight:700;font-size:8.5px;width:56px;height:21px;display:flex;align-items:center;justify-content:center;text-align:center;line-height:1}

.band{left:0;right:0;top:492px;height:111px;background:var(--black)}
.points{left:23px;width:446px;top:463px;height:93px;background:var(--red);border-radius:15px;display:flex;align-items:center}
.point{flex:1;text-align:center;font-size:12.5px;font-weight:700;line-height:1.3;padding:0 6px}
.point + .point{border-left:1px solid rgba(0,0,0,.25)}
.point:first-child{flex:1.15}
.point:last-child{flex:1.15}
.trust{top:568px;font-size:21px;font-weight:800;color:var(--white);display:flex;align-items:center;justify-content:center;gap:8px}
.trust em{font-style:normal;color:var(--red)}
.trust svg{width:20px;height:20px}

.cta{left:29px;top:622px;font-size:25px;font-weight:800;color:var(--red);line-height:1}
.phone{display:flex;align-items:center;gap:8px;font-weight:800;color:var(--black);line-height:1}
.phone__icon{width:26px;height:26px;border-radius:50%;background:var(--red);display:flex;align-items:center;justify-content:center}
.phone__icon svg{width:15px;height:15px}
.front-phone{left:248px;top:624px;font-size:34px}
.front-url{left:248px;top:661px;font-size:15px;font-weight:800}
.front-url b,.red{color:var(--red)}

/* back */
.trusted{left:0;right:0;top:0;height:121px;background:var(--red)}
.trusted__small{top:22px;font-size:30px;font-weight:800;color:var(--white);letter-spacing:8px;padding-left:8px}
.trusted__big{top:58px;font-family:"Krona One",sans-serif;font-size:21px;line-height:1.15;color:var(--black)}

.included{left:32px;top:146px;width:428px;height:154px;border:1px solid var(--line);border-radius:14px}
.included__title{top:134px;left:0;right:0;text-align:center}
.included__title span{background:var(--white);padding:0 12px;font-size:23px;font-weight:800}
.inc{font-size:12.5px;font-weight:700;line-height:1.3;display:flex;gap:5px;align-items:flex-start}
.inc svg{width:11px;height:11px;flex:none;margin-top:3px}
.inc--l{text-align:right;right:293px}
.inc--r{left:296px}
.inc-mark{left:212px;top:195px;width:66px;height:66px;border-radius:50%;background:var(--red)}

.why__title{left:39px;top:310px;font-size:24px;font-weight:800;color:var(--red)}
.why__list{left:39px;top:345px;list-style:none}
.why__list li{display:flex;align-items:center;gap:6px;font-size:12.5px;font-weight:700;height:20px}
.why__list svg{width:10px;height:10px}

.ideal{left:300px;top:315px;width:160px;height:245px;border-radius:14px;overflow:hidden;background:var(--red)}
.ideal__head{height:50px;background:var(--black);color:var(--white);font-size:24px;font-weight:800;display:flex;align-items:center;justify-content:center}
.ideal__item{margin:0 14px;border-bottom:1px solid rgba(255,255,255,.6);color:var(--white);text-align:center;font-size:14px;font-weight:800;line-height:1.2;display:flex;align-items:center;justify-content:center}
.ideal__item:last-child{border-bottom:none}

.areas{left:0;width:300px;top:465px;height:50px;background:var(--black)}
.areas__tag{left:44px;top:451px;height:26px;padding:0 13px;background:var(--red);color:var(--white);border-radius:0 10px 0 0;font-size:16px;font-weight:800;letter-spacing:1.5px;display:flex;align-items:center}
.areas__big{left:44px;top:482px;font-family:"Krona One",sans-serif;font-size:26px;color:var(--white);line-height:1}
.closing{left:44px;top:521px;font-size:17px;font-weight:800;color:var(--red);line-height:1.05}

.rule{left:44px;width:212px;height:1px;background:#999}
.bulk{left:44px;top:574px;display:flex;gap:7px;align-items:center;font-size:12.5px;font-weight:800;line-height:1.1}
.bulk svg{width:26px;height:26px}
.back-phone{left:44px;top:620px;font-size:32px}
.back-brand{left:290px;top:594px}
.back-brand .brand__dot{width:30px;height:30px}
.back-brand .brand__name{font-size:21px}
.contacts{left:42px;top:656px;display:flex;gap:13px;font-size:13px;font-weight:800}
.contacts span{display:flex;align-items:center;gap:4px}
.contacts svg{width:11px;height:11px}
</style>
</head>
<body>

<section class="page page--front">
  <div class="abs brand front-brand"><span class="brand__dot"></span><span class="brand__name">Grill Shine Crew</span></div>
  <div class="abs center kicker">PROFESSIONAL</div>
  <h1 class="abs center headline">BBQ CLEANING</h1>
  <div class="abs center subhead">FOR SHARED &amp; COMMUNAL AREAS</div>
  <p class="abs center tagline">Keep your BBQs clean, safe, and ready for residents and guests</p>

  <div class="abs photo photo--before" role="img" aria-label="Photo of a greasy, dirty stainless steel BBQ before cleaning">
    <div class="photo__tab"><span>BEFORE</span></div>
    <div class="chips"><span class="chip">GREASY</span><span class="chip">DIRTY</span><span class="chip">UNSAFE</span></div>
  </div>
  <div class="abs photo photo--after" role="img" aria-label="Photo of the same stainless steel BBQ after cleaning">
    <div class="photo__tab"><span>AFTER</span></div>
    <div class="chips"><span class="chip">CLEAN</span><span class="chip">HYGIENIC</span><span class="chip">READY<br>TO USE</span></div>
  </div>

  <div class="abs band"></div>
  <div class="abs points">
    <div class="point">Deep clean of grills, burners and internal components</div>
    <div class="point">Multiple BBQs cleaned in one visit</div>
    <div class="point">Ideal for retirement villages, resorts and body corporate</div>
  </div>
  <div class="abs center trust">
    <svg viewBox="0 0 20 20" fill="none" stroke="#d7263d" stroke-width="1.8"><path d="M10 2l7 3v5c0 4-3 7-7 8-4-1-7-4-7-8V5z"/><path d="M7 10l2 2 4-4"/></svg>
    <span>FULLY INSURED <em>AND</em> POLICE CHECKED</span>
    <svg viewBox="0 0 20 20" fill="none" stroke="#d7263d" stroke-width="1.8"><rect x="3" y="2" width="11" height="15" rx="1"/><path d="M6 6h5M6 9h5M6 12h3"/><circle cx="14" cy="14" r="3"/><path d="M16 16l2 2"/></svg>
  </div>

  <div class="abs cta">GET A QUOTE OR<br>BOOK A SERVICE</div>
  <div class="abs phone front-phone">
    <span class="phone__icon"><svg viewBox="0 0 24 24" fill="#fff"><path d="M6.6 10.8a15 15 0 006.6 6.6l2.2-2.2a1 1 0 011-.25 11.4 11.4 0 003.6.6 1 1 0 011 1V20a1 1 0 01-1 1A17 17 0 013 4a1 1 0 011-1h3.5a1 1 0 011 1c0 1.25.2 2.45.6 3.6a1 1 0 01-.25 1z"/></svg></span>
    <span>0428 593 214</span>
  </div>
  <div class="abs front-url">www.<b>grillshinecrew</b>.example.au</div>
</section>

<section class="page page--back">
  <div class="abs trusted"></div>
  <div class="abs center trusted__small">TRUSTED BY</div>
  <h2 class="abs center trusted__big">PROPERTY MANAGERS<br>&amp; FACILITIES TEAMS</h2>

  <div class="abs included"></div>
  <div class="abs included__title"><span>WHAT’S INCLUDED</span></div>
  <div class="abs inc inc--l" style="top:180px"><span>FULL DISMANTLE<br>AND DEEP CLEAN</span><svg viewBox="0 0 12 12" fill="none" stroke="#d7263d" stroke-width="1.3"><circle cx="6" cy="6" r="5"/><path d="M3.5 6l1.8 1.8L8.5 4.5"/></svg></div>
  <div class="abs inc inc--l" style="top:231px"><span>REMOVAL OF<br>GREASE, CARBON &amp;<br>BUILT-UP RESIDUE</span><svg viewBox="0 0 12 12" fill="none" stroke="#d7263d" stroke-width="1.3"><circle cx="6" cy="6" r="5"/><path d="M3.5 6l1.8 1.8L8.5 4.5"/></svg></div>
  <div class="abs inc-mark"></div>
  <div class="abs inc inc--r" style="top:180px"><svg viewBox="0 0 12 12" fill="none" stroke="#d7263d" stroke-width="1.3"><circle cx="6" cy="6" r="5"/><path d="M3.5 6l1.8 1.8L8.5 4.5"/></svg><span>GRILLS, BURNERS,<br>TRAYS &amp; SURFACES<br>CLEANED</span></div>
  <div class="abs inc inc--r" style="top:247px"><svg viewBox="0 0 12 12" fill="none" stroke="#d7263d" stroke-width="1.3"><circle cx="6" cy="6" r="5"/><path d="M3.5 6l1.8 1.8L8.5 4.5"/></svg><span>REASSEMBLED AND<br>CHECKED</span></div>

  <h3 class="abs why__title">WHY CHOOSE US:</h3>
  <ul class="abs why__list">
    <li><svg viewBox="0 0 12 12" fill="none" stroke="#d7263d" stroke-width="1.3"><circle cx="6" cy="6" r="5"/><path d="M3.5 6l1.8 1.8L8.5 4.5"/></svg>Professional, reliable service</li>
    <li><svg viewBox="0 0 12 12" fill="none" stroke="#d7263d" stroke-width="1.3"><circle cx="6" cy="6" r="5"/><path d="M3.5 6l1.8 1.8L8.5 4.5"/></svg>Works around your schedule</li>
    <li><svg viewBox="0 0 12 12" fill="none" stroke="#d7263d" stroke-width="1.3"><circle cx="6" cy="6" r="5"/><path d="M3.5 6l1.8 1.8L8.5 4.5"/></svg>Ideal for high-use communal BBQs</li>
    <li><svg viewBox="0 0 12 12" fill="none" stroke="#d7263d" stroke-width="1.3"><circle cx="6" cy="6" r="5"/><path d="M3.5 6l1.8 1.8L8.5 4.5"/></svg>One-off or ongoing maintenance</li>
    <li><svg viewBox="0 0 12 12" fill="none" stroke="#d7263d" stroke-width="1.3"><circle cx="6" cy="6" r="5"/><path d="M3.5 6l1.8 1.8L8.5 4.5"/></svg>Fully insured &amp; police checked</li>
  </ul>

  <div class="abs ideal">
    <div class="ideal__head">IDEAL FOR</div>
    <div class="ideal__item" style="height:52px">RETIREMENT<br>VILLAGES</div>
    <div class="ideal__item" style="height:50px">APARTMENT<br>COMPLEXES</div>
    <div class="ideal__item" style="height:35px">RESORT</div>
    <div class="ideal__item" style="height:52px">BODY CORPORATE<br>PROPERTIES</div>
  </div>

  <div class="abs areas"></div>
  <div class="abs areas__tag">KEEP YOUR SHARED</div>
  <div class="abs areas__big">BBQ AREAS</div>
  <div class="abs closing">CLEAN, SAFE, &amp;<br>PRESENTABLE YEAR-ROUND</div>

  <div class="abs rule" style="top:567px"></div>
  <div class="abs bulk">
    <svg viewBox="0 0 26 26" fill="none" stroke="#0b0b0b" stroke-width="1.4"><rect x="2" y="4" width="20" height="16" rx="1"/><path d="M2 8h20M5 11h3M10 11h3M15 11h3M5 15h3M10 15h3"/><path d="M16 16l6 6" stroke="#d7263d"/></svg>
    <span>BULK BOOKINGS AVAILABLE<br>FOR <span class="red">MULTIPLE BBQs</span></span>
  </div>
  <div class="abs rule" style="top:610px"></div>
  <div class="abs phone back-phone">
    <span class="phone__icon"><svg viewBox="0 0 24 24" fill="#fff"><path d="M6.6 10.8a15 15 0 006.6 6.6l2.2-2.2a1 1 0 011-.25 11.4 11.4 0 003.6.6 1 1 0 011 1V20a1 1 0 01-1 1A17 17 0 013 4a1 1 0 011-1h3.5a1 1 0 011 1c0 1.25.2 2.45.6 3.6a1 1 0 01-.25 1z"/></svg></span>
    <span>0428 593 214</span>
  </div>
  <div class="abs brand back-brand"><span class="brand__dot"></span><span class="brand__name">Grill Shine<br>Crew</span></div>
  <div class="abs contacts">
    <span><svg viewBox="0 0 12 12" fill="none" stroke="#d7263d" stroke-width="1.2"><circle cx="6" cy="6" r="5"/><path d="M1 6h10M6 1c-2.5 3-2.5 7 0 10M6 1c2.5 3 2.5 7 0 10"/></svg>www.grillshinecrew.example.au</span>
    <span><svg viewBox="0 0 12 12" fill="none" stroke="#d7263d" stroke-width="1.2"><rect x="1" y="2.5" width="10" height="7" rx="1"/><path d="M1 3l5 4 5-4"/></svg>grillshinecrew@mailbox.example</span>
  </div>
</section>

</body>
</html>
```